WP website design (Whitlock)

We need a wordpress design for an established auction and real estate company based in Daswon Creek, Canada. The winning design will incorporate a professional color scheme with company logo in a clean layout with specified widgets. The design needs to consider that this will be developed on a responsive theme. Colors will complement logo - red, black and gray.

Industry/Entity Type

Real Estate

Font styles to use
Sans Serif

Requirements
Must have
• Must Have:
the main logo is provided and the 'horse' logo shouldbe incorporated into the hearder or sidebar (either left or right)as well. Contact info should be placed in the header, and footer too: (250) 555-0143
(250) 555-0178
(250) 555-0192
rvm@zorquil.bc.ca

- Navigation:
1) Home 2) Auctions 3) Online Auctions 4) About Us 5) Contact Us

Home Page will have following:
"Family owned and operated with a family guarantee.
Located in Dawson Creek, B.C. Canada

Competitive Rates Bonded & Licensed Livestock Dealers & Auctioneers
All Types of Auction Sales in B.C. & Alberta

Farm, Machinery
Equipment Sales
Household & Estate Sales
Livestock Marketing Consultants
Field Cattle Sales
Livestock Pedigree Sales
Horse Sales Appraisals"

Homepage will have auctions - as at http://brindlevexsales.com/upcoming-auctions/.

Footer will have smaller company logo, credit card logo, and attached association logos and this contact info:
.(620) 555-0117: OFFICE
(620) 555-0164: FAX
hgrup@vxq.com: email
Address: 718 N. Birch Ave., Johnson KS
Mailing Address: PO Box 839, Johnson, KS

Widgets:
1) email sign up 2) News blog widget 3) testimonial blog widget 4) featured auctions widget 5) the 'Gold Peg' logo which is included
Nice to have
• Nice to Have:
- demonstrate the drop-down menu styling, e.g. under Auctions
- Upcoming Auctions
- Past Auctions

```html
<!DOCTYPE html>
<html lang="en">
<head>
<meta charset="utf-8">
<title>Whitlock's Auction Mart Ltd.</title>
<link href="https://fonts.googleapis.com/css2?family=Open+Sans:wght@400;600;700&family=Arimo:wght@400;700&family=Oswald:wght@400;500&display=swap" rel="stylesheet">
<style>
:root{
  --red:#e3262b;
  --red-dark:#c81e23;
  --ink:#333333;
  --charcoal:#3a3a3a;
  --page:#ebebeb;
  --panel:#f3f3f3;
  --line:#dcdcdc;
  --white:#ffffff;
  --text:#3c3c3c;
}
*{margin:0;padding:0;box-sizing:border-box}
html,body{width:812px;height:1200px;overflow:hidden}
body{background:var(--page);font-family:"Arimo",Arial,sans-serif;color:var(--text);position:relative}
.abs{position:absolute}
.site-header{position:absolute;left:0;top:0;width:812px;height:121px;background:var(--white)}
.brand{left:88px;top:14px;width:110px;text-align:center;font-family:"Open Sans",sans-serif;font-weight:700;font-size:12px;line-height:15px;color:var(--ink);letter-spacing:.2px}
.brand-dot{display:block;width:14px;height:14px;border-radius:50%;background:var(--red);margin:6px auto 0}
.tollfree{left:497px;top:27px;width:223px;height:29px;border-top:1px dotted #999;border-bottom:1px dotted #999;display:flex;align-items:center;gap:5px;white-space:nowrap;font-family:"Oswald",sans-serif;font-size:12.5px;color:var(--ink)}
.tollfree .phone-icon{flex:none;width:19px;height:19px;background:var(--red);border-radius:2px;display:flex;align-items:center;justify-content:center}
.tollfree strong{color:var(--red);font-weight:400;font-size:16px;margin-left:2px}
.main-nav{left:68px;top:87px;width:677px;height:34px;background:linear-gradient(#e8343a,var(--red-dark));border-radius:5px 5px 0 0}
.main-nav a{position:absolute;top:0;height:34px;line-height:34px;color:var(--white);font-family:"Open Sans",sans-serif;font-weight:600;font-size:10px;text-decoration:none;white-space:nowrap}
.nav-sep{position:absolute;top:4px;width:1px;height:26px;background:rgba(0,0,0,.15);box-shadow:1px 0 0 rgba(255,255,255,.15)}
.social{position:absolute;top:8px;width:18px;height:18px;border-radius:50%}
.content{left:68px;top:121px;width:677px;height:997px;background:var(--white)}
.hero{left:76px;top:129px;width:662px;height:300px;border:3px solid #111;background:linear-gradient(180deg,#2f6fc4 0%,#7fb0e8 30%,#efe9dc 55%,#d9d2c0 80%,#5d7a3a 100%)}
.welcome-title{left:94px;top:446px;font-family:"Open Sans",sans-serif;font-weight:400;font-size:13.5px;color:var(--ink);white-space:nowrap}
.welcome-text{left:95px;top:477px;width:400px;font-size:8.6px;line-height:12.2px}
.feature-box{width:405px;height:169px;background:var(--panel);border:1px solid var(--line);border-radius:3px}
.feature-head{position:absolute;left:-1px;top:-1px;right:-1px;height:28px;background:var(--red);color:var(--white);font-family:"Open Sans",sans-serif;font-size:11.5px;line-height:28px;padding-left:8px;border-radius:2px 2px 0 0;white-space:nowrap}
.thumb{position:absolute;border:2px solid var(--white);box-shadow:0 0 2px rgba(0,0,0,.3)}
.lot-title{position:absolute;color:var(--red);font-size:9.5px;white-space:nowrap}
.lot-text{position:absolute;font-size:9.3px;line-height:12.2px}
.lot-small{position:absolute;font-size:8.3px;line-height:12.4px}
.btn{position:absolute;width:58px;height:18px;border-radius:4px;color:var(--white);font-size:8px;font-weight:700;display:flex;align-items:center;justify-content:center;gap:5px}
.btn.red{background:var(--red)}
.btn.dark{background:var(--charcoal)}
.btn i{display:block;width:9px;height:7px;background:var(--white);border-radius:1px}
.tab{height:28px;line-height:28px;font-family:"Open Sans",sans-serif;font-size:11.5px;color:var(--white);padding-left:11px;white-space:nowrap}
.side-box{left:540px;width:179px;background:var(--panel);border:1px solid var(--line);border-radius:3px}
.side-head{position:absolute;left:-1px;top:-1px;right:-1px;height:21px;background:var(--charcoal);color:var(--white);font-family:"Open Sans",sans-serif;font-size:11px;line-height:21px;padding-left:14px;white-space:nowrap}
.field{position:absolute;left:14px;width:143px;height:16px;background:var(--white);border-radius:3px}
.signup{position:absolute;left:110px;top:75px;width:47px;height:16px;border-radius:7px;background:#1e1e1e;color:var(--white);font-size:8.5px;text-align:center;line-height:16px}
.red-date{position:absolute;color:var(--red);font-size:8.8px;white-space:nowrap}
.bold-date{position:absolute;color:var(--red);font-size:8.2px;font-weight:700;white-space:nowrap}
.side-text{position:absolute;font-size:8.3px;line-height:12.4px}
.more{position:absolute;color:var(--red);font-size:8.3px;font-style:italic}
.gold-peg{position:absolute;left:19px;top:144px;width:143px;height:64px;border:2px solid #111;background:var(--white);text-align:center;font-family:"Arimo",sans-serif;font-weight:700;color:var(--red)}
.gold-peg .name{font-size:20px;line-height:32px;margin-top:6px}
.gold-peg .sub{font-size:8.5px}
.quote{position:absolute;left:8px;top:32px;width:168px;font-size:8.3px;line-height:13.4px}
.quote b{color:#aaa;font-family:"Open Sans",sans-serif;font-size:13px;font-weight:700;line-height:0}
.site-footer{left:0;top:1118px;width:812px;height:82px;background:#353535;border-top:3px solid var(--red)}
.footer-links{left:94px;top:27px;font-size:8.5px;color:var(--white);word-spacing:1px;white-space:nowrap}
.footer-links span{margin:0 10px}
.copyright{left:94px;top:52px;font-size:8.5px;color:var(--white);white-space:nowrap}
.footer-brand{left:640px;top:8px;width:80px;text-align:center;font-family:"Open Sans",sans-serif;font-weight:700;font-size:9px;line-height:12px;color:var(--white)}
.card{position:absolute;top:61px;height:17px;border:1px solid #ccc;border-radius:2px}
</style>
</head>
<body>

<header class="site-header">
  <div class="abs brand">WHITLOCK'S AUCTION<br>MART LTD.<span class="brand-dot"></span></div>
  <div class="abs tollfree">
    <span class="phone-icon"><svg width="12" height="12" viewBox="0 0 24 24"><path fill="#fff" d="M6.6 10.8a15 15 0 0 0 6.6 6.6l2.2-2.2c.3-.3.7-.4 1-.2 1.1.4 2.3.6 3.6.6.6 0 1 .4 1 1V20c0 .6-.4 1-1 1A17 17 0 0 1 3 4c0-.6.4-1 1-1h3.5c.6 0 1 .4 1 1 0 1.3.2 2.5.6 3.6.1.3 0 .7-.2 1z"/></svg></span>
    <span>CALL US TOLL-FREE ON</span><strong>1800 555 014</strong>
  </div>
  <nav class="abs main-nav">
    <a style="left:24px">HOME</a>
    <span class="nav-sep" style="left:73px"></span>
    <a style="left:99px">AUCTIONS</a>
    <span class="nav-sep" style="left:175px"></span>
    <a style="left:203px">ONLINE AUCTIONS</a>
    <span class="nav-sep" style="left:319px"></span>
    <a style="left:348px">ABOUT US</a>
    <span class="nav-sep" style="left:423px"></span>
    <a style="left:451px">CONTACT US</a>
    <span class="social" style="left:562px;background:#3b5fa0"></span>
    <span class="social" style="left:586px;background:#3fb5e8"></span>
    <span class="social" style="left:609px;background:#f19a26"></span>
    <span class="social" style="left:633px;background:#2b8fc9"></span>
  </nav>
</header>

<main class="abs content"></main>

<div class="abs hero" role="img" aria-label="Photo of a large white Mediterranean villa with terracotta roof under a blue sky"></div>

<h1 class="abs welcome-title">WELCOME TO WHITLOCK'S AUCTIONS MART LTD.</h1>
<p class="abs welcome-text">Lorem Ipsum is that it has a more-or-less normal distribution of letters, as opposed to using 'Content here, content here', making it look like readable English. Many desktop publishing packages and web page editors now use Lorem Ipsum as their default model text, and a search for 'lorem ipsum' will uncover many web sites still in their infancy.</p>

<section class="abs feature-box" style="left:92px;top:556px">
  <div class="feature-head">FAMILY OWNED AND OPERATED WITH A FAMILY GUARANTEE</div>
  <div class="thumb" role="img" aria-label="Photo of a hand holding house keys in front of a home" style="left:8px;top:36px;width:81px;height:60px;background:linear-gradient(135deg,#3d7fd1,#c8b8a0 60%,#8a6a4a)"></div>
  <div class="lot-title" style="left:106px;top:43px">FURNITURE ' ANTIQUES ' COLLECTIBLES</div>
  <p class="lot-text" style="left:106px;top:55px;width:280px">Lorem Ipsum is that it has a more-or-less normal distribution of letters, as opposed to using 'Content here, content here', making it look like readable English. Many desktop publish-</p>
  <div class="btn red" style="left:19px;top:114px"><i></i>Details</div>
  <div class="btn dark" style="left:19px;top:137px"><i></i>Photos</div>
  <div class="lot-title" style="left:106px;top:119px">LIVE ON-SITE AUCTION</div>
  <p class="lot-small" style="left:106px;top:136px;width:200px">Lorem Ipsum is that it has a more-or-less normal distribution of letters,</p>
</section>

<section class="abs feature-box" style="left:94px;top:749px">
  <div class="feature-head">FAMILY OWNED AND OPERATED WITH A FAMILY GUARANTEE</div>
  <div class="thumb" role="img" aria-label="Photo of a hand holding house keys in front of a home" style="left:8px;top:36px;width:81px;height:60px;background:linear-gradient(135deg,#3d7fd1,#c8b8a0 60%,#8a6a4a)"></div>
  <div class="lot-title" style="left:106px;top:43px">FURNITURE ' ANTIQUES ' COLLECTIBLES</div>
  <p class="lot-small" style="left:106px;top:55px;width:280px">Lorem Ipsum is that it has a more-or-less normal distribution of letters, as opposed to using 'Content here, content here', making it look like readable English. Many desktop publishing packages and</p>
  <div class="btn red" style="left:19px;top:114px"><i></i>Details</div>
  <div class="btn dark" style="left:19px;top:137px"><i></i>Photos</div>
  <div class="lot-title" style="left:106px;top:119px">LIVE ON-SITE AUCTION</div>
  <p class="lot-small" style="left:106px;top:136px;width:200px">Lorem Ipsum is that it has a more-or-less normal distribution of letters,</p>
</section>

<section class="abs feature-box" style="left:94px;top:944px;height:148px">
  <div class="abs tab" style="left:-1px;top:-1px;width:143px;background:var(--red)">FEATURED AUCTIONS</div>
  <div class="abs tab" style="left:144px;top:-1px;width:146px;background:var(--charcoal)">UPCOMING AUCTIONS</div>
  <div class="abs" role="img" aria-label="Photo of a brick family house with green lawn" style="left:6px;top:45px;width:137px;height:76px;background:linear-gradient(180deg,#9cc4e6 0%,#a4735a 45%,#7e5a48 70%,#4f7c35 100%)"></div>
  <p class="lot-small" style="left:155px;top:44px;width:235px">Lorem Ipsum is that it has a more-or-less normal distribution of letters, as opposed to using 'Content here, content here', making it look like readable English. Many desktop publishing packages and web page editors now use Lorem Ipsum as their default model text, and a search</p>
</section>

<aside>
  <section class="abs side-box" style="top:444px;height:94px">
    <div class="side-head">EMAIL SIGN UP FROM</div>
    <div class="field" style="top:28px"></div>
    <div class="field" style="top:52px"></div>
    <div class="signup">Sign up</div>
  </section>

  <section class="abs side-box" style="top:556px;height:160px">
    <div class="side-head">ASSET FOR SALE FADER</div>
    <div class="abs" role="img" aria-label="Photo of a suburban two-storey house" style="left:21px;top:30px;width:137px;height:62px;border:2px solid #fff;background:linear-gradient(180deg,#5fa2e0 0%,#b58a6e 50%,#5a7f3a 100%)"></div>
    <div class="red-date" style="left:14px;top:102px">Saturday March 16, 2014 at 10;30 am</div>
    <p class="side-text" style="left:16px;top:113px;width:155px">Lorem Ipsum is that it has a more-or-less normal distribution of letters, as opposed using</p>
    <div class="more" style="left:113px;top:142px">More Detail ››</div>
  </section>

  <section class="abs side-box" style="top:735px;height:227px">
    <div class="side-head">NEWS BLOPG</div>
    <div class="abs" role="img" aria-label="Photo of a house" style="left:10px;top:32px;width:56px;height:38px;border:2px solid #fff;background:linear-gradient(180deg,#6aa8e0,#d9c89a 55%,#5f8240)"></div>
    <div class="bold-date" style="left:76px;top:32px">Saturday march 6, 2014</div>
    <p class="side-text" style="left:77px;top:44px;width:90px">Lorem Ipsum is that it has a more-or-less</p>
    <div class="abs" role="img" aria-label="Photo of a house" style="left:11px;top:82px;width:56px;height:38px;border:2px solid #fff;background:linear-gradient(180deg,#6aa8e0,#d9c89a 55%,#5f8240)"></div>
    <div class="bold-date" style="left:77px;top:82px">Saturday march 6, 2014</div>
    <p class="side-text" style="left:78px;top:94px;width:90px">Lorem Ipsum is that it has a more-or-less</p>
    <div class="gold-peg"><div class="name">Gold Peg</div><div class="sub">Click here for online bidding</div></div>
  </section>

  <section class="abs side-box" style="top:977px;height:114px">
    <div class="side-head" style="text-align:center;padding-left:0">Clients Testimonials</div>
    <p class="quote"><b>“</b> &nbsp;Lorem Ipsum is that it has a more-or-less normal distribution of letters, as opposed to using 'Content here, content here', making it look like readable English. <b>”</b></p>
  </section>
</aside>

<footer class="abs site-footer">
  <div class="abs footer-links">Home<span>I</span>Auctions<span>I</span>Online Auctions<span>I</span>About Us<span>I</span>Contact Us</div>
  <div class="abs copyright">Copyright (c) Whitlock's Auction &nbsp;.2014. All Right Reserved</div>
  <div class="abs" role="img" aria-label="Horse head emblem" style="left:607px;top:4px;width:30px;height:52px;background:linear-gradient(180deg,#222,#0c0c0c);border-radius:3px"></div>
  <div class="abs footer-brand">WHITLOCK'S AUCTION<br>MART LTD.</div>
  <span class="card" style="left:582px;width:27px;background:#fff"></span>
  <span class="card" style="left:612px;width:27px;background:#d8d8d8"></span>
  <span class="card" style="left:642px;width:27px;background:#e6edf5"></span>
  <span class="card" style="left:672px;width:48px;background:#fff"></span>
</footer>

</body>
</html>
```